KORVa: AI driven decarbonization application

We are seeking an engaging, user-friendly, and visually appealing user interface for our B2B SaaS platform, Brelmont KORVa. This solution helps large organizations achieve net-zero emissions using AI-driven forecasting, AI models, a emission mitigation library, and a scenario simulator..

A big challenge is to allow the user to work efficiently with multidimensional data.

Requirements:

* Design a modern, professional, and visually striking user interface, catering to a diverse audience within large corporations, including executives, strategists, and environmental specialists.

* Construct an intuitive navigation system, allowing users to seamlessly access functionalities for informed decision-making and tracking progress towards net-zero emissions.

* The application is expected to be used on desktops first

* Incorporate our brand's colors, and visual elements into the design to maintain consistency throughout the application.

* Provide design assets and documentation, such as style guides, design specifications, and necessary assets (e.g., icons, illustrations) for our development team to implement the design. We use Figma and would appreciate delivery as figma files.

Please note that we also need more pages over time. The most important is to get the work bench page right. We will also need:
* a landing page where the users can select previous scenarios and see some high level data.
* A page with information on historical data per asset
* An analytics page
* User and system administration pages.
These pages are out of scope for this project, but they should be available in the navigation solution.

Please submit your initial design concepts, accompanied by a brief explanation of your approach and the rationale behind your design choices. We will offer feedback and collaborate with the chosen designer to refine the design, ensuring it meets our requirements and vision.

We are really hoping to see some elegant user interfaces. The functionality describe in the attachment is important, but the layout is not. Feel free to invent.

Attached files:

Target Market(s)

Energy intensive industries

Requirements
Must have
• Easy to navigate through the different data dimensions: Time, assets, mitigation measures, and advanced details under mitigation measures. The design in the attached files are just our working drafts. Creative alternatives are very welcome.
Nice to have
• Elegant layouts that differ from our working drafts.

```html
<!DOCTYPE html>
<html lang="en">
<head>
<meta charset="utf-8">
<title>Brelmont KORVa – Workbench concepts</title>
<link href="https://fonts.googleapis.com/css2?family=Roboto:wght@300;400;500;700&display=swap" rel="stylesheet">
<style>
  :root{
    --page:#f2f2f2;
    --chrome:#0a0a0a;
    --search:#2b2b2b;
    --panel:#ffffff;
    --ink:#2a2a2a;
    --muted:#777;
    --grid:#e8e8e8;
    --teal:#5b8e8f;
    --teal-dark:#3f7475;
    --brand-blue:#3d7fb6;
    --blue:#1d5a97;
    --field:#e9eef3;
    --red-line:#e8917f;
    --purple-line:#35288c;
    --sky-line:#4b8fe3;
    --overage:#e02525;
    --goals:#2e9a4d;
    --card-orange:#e3815e;
    --card-yellow:#e7c33a;
    --card-navy:#3d5c95;
    --bar-red:#e2645a;
    --bar-orange:#e3835f;
    --bar-green:#86c28c;
    --bar-yellow:#e6c63b;
    --bar-blue:#4f86f0;
    --bar-slate:#465f95;
    --bar-violet:#8a4cf0;
  }
  *{box-sizing:border-box;margin:0;padding:0}
  html,body{width:1200px;height:1008px;overflow:hidden;background:var(--page);font-family:'Roboto',Arial,sans-serif;color:var(--ink)}
  .board{position:absolute;left:0;top:0;width:2100px;height:1764px;transform:scale(.5714);transform-origin:0 0}
  svg text{font-family:'Roboto',Arial,sans-serif}
  .screen{position:absolute;width:596px;background:var(--panel);box-shadow:0 6px 24px rgba(0,0,0,.12);overflow:hidden}
  .topbar{position:absolute;left:0;top:0;right:0;height:38px;background:var(--chrome)}
  .brand{position:absolute;left:10px;top:7px;font-size:21px;font-weight:300;letter-spacing:2px;color:var(--brand-blue)}
  .search{position:absolute;left:336px;top:11px;width:137px;height:17px;background:var(--search);border-radius:2px;color:#cfcfcf;font-size:7px;line-height:17px;padding-left:8px}
  .search svg{position:absolute;right:7px;top:4px}
  .tool-icon{position:absolute;top:10px;width:18px;height:18px;border-radius:50%}
  .tool-icon.chart{left:496px;background:#3a3a3a}
  .tool-icon.chart svg{position:absolute;left:4px;top:4px}
  .tool-icon.avatar{left:521px;background:radial-gradient(circle at 50% 40%,#d8b9a0,#8a6a55)}
  .sidebar{position:absolute;left:0;top:38px;width:127px;bottom:0;background:var(--chrome);padding-top:1px}
  .nav-item{height:30.7px;line-height:30.7px;padding-left:17px;font-size:7.6px;color:#f2f2f2;white-space:nowrap}
  .nav-item.active{background:var(--teal);border-left:3px solid var(--teal-dark);padding-left:14px}
  .content{position:absolute;left:127px;top:38px;right:0;bottom:0}
  .abs{position:absolute}
  .h-title{font-size:10px;font-weight:500;color:#333}
  .assets-title{font-size:10px;font-weight:700;color:var(--blue)}
  .filters{display:flex;align-items:center;gap:4px}
  .filters span.label{font-size:7px;font-weight:500;margin-right:4px}
  .chip{background:#e4e8ec;font-size:5.2px;padding:3px 5px;border-radius:1px}
  .insert{width:54px;height:19px;background:var(--teal);color:#fff;font-size:7px;font-weight:700;text-align:center;line-height:19px;border-radius:1px}
  .param-label{font-size:7.4px;font-weight:500}
  .param-value{width:63px;height:14px;background:var(--field);font-size:7px;color:#555;text-align:center;line-height:14px}
  .param-check{width:16px;height:14px;background:var(--field)}
  .divider{width:1px;background:#ececec}
  .legend{display:flex;gap:20px;font-size:7px;color:#444}
  .legend i{display:inline-block;width:5px;height:5px;border-radius:50%;margin-right:5px;vertical-align:middle}
  .scenario-card{position:absolute;height:39px;color:#fff;padding:7px 0 0 14px;box-shadow:0 3px 8px rgba(0,0,0,.15)}
  .scenario-card b{display:block;font-size:10px;font-weight:500}
  .scenario-card small{display:block;font-size:7px;margin-top:3px;opacity:.9}
  .scenario-card svg{position:absolute;right:11px;top:13px}
  .card-teal{background:var(--teal)}
  .card-orange{background:var(--card-orange)}
  .card-yellow{background:var(--card-yellow)}
  .card-navy{background:var(--card-navy)}
  .gantt-bar{position:absolute;height:17px;font-size:7.4px;color:#fff;line-height:17px;padding-left:12px;border-radius:1px}
</style>
</head>
<body>
<svg width="0" height="0" style="position:absolute" aria-hidden="true">
  <defs>
    <symbol id="asset-table" viewBox="0 0 250 170">
      <g font-size="5.2" fill="#333">
        <g id="row-base">
          <text x="1" y="4">Lorem ipsum</text><text x="46" y="4">Field</text><text x="71" y="4">Lorem ipsum</text><text x="116" y="4">Sed ut perspiciatis</text><text x="172" y="4">100%</text><text x="197" y="4">Producing</text>
        </g>
        <use href="#row-base" y="17"/><use href="#row-base" y="34"/><use href="#row-base" y="51"/><use href="#row-base" y="68"/><use href="#row-base" y="85"/><use href="#row-base" y="102"/><use href="#row-base" y="119"/><use href="#row-base" y="136"/><use href="#row-base" y="153"/>
      </g>
      <g fill="#fff" stroke="#bbb" stroke-width=".6">
        <rect x="233" y="-1" width="6" height="6"/><rect x="233" y="33" width="6" height="6"/><rect x="233" y="67" width="6" height="6"/><rect x="233" y="84" width="6" height="6"/><rect x="233" y="101" width="6" height="6"/><rect x="233" y="118" width="6" height="6"/><rect x="233" y="152" width="6" height="6"/><rect x="233" y="169" width="6" height="6"/>
      </g>
      <g fill="#1d5a97"><rect x="233" y="16" width="6" height="6"/><rect x="233" y="50" width="6" height="6"/><rect x="233" y="135" width="6" height="6"/></g>
    </symbol>

    <symbol id="emission-chart" viewBox="0 0 440 215">
      <g stroke="#e8e8e8" stroke-width=".7">
        <line x1="26" y1="5" x2="420" y2="5"/><line x1="26" y1="35.8" x2="420" y2="35.8"/><line x1="26" y1="66.7" x2="420" y2="66.7"/><line x1="26" y1="97.5" x2="420" y2="97.5"/><line x1="26" y1="128.3" x2="420" y2="128.3"/><line x1="26" y1="159.2" x2="420" y2="159.2"/><line x1="26" y1="190" x2="420" y2="190"/>
        <line x1="26" y1="5" x2="26" y2="190"/><line x1="61.8" y1="5" x2="61.8" y2="190"/><line x1="97.6" y1="5" x2="97.6" y2="190"/><line x1="133.5" y1="5" x2="133.5" y2="190"/><line x1="169.3" y1="5" x2="169.3" y2="190"/><line x1="205.1" y1="5" x2="205.1" y2="190"/><line x1="240.9" y1="5" x2="240.9" y2="190"/><line x1="276.7" y1="5" x2="276.7" y2="190"/><line x1="312.6" y1="5" x2="312.6" y2="190"/><line x1="348.4" y1="5" x2="348.4" y2="190"/><line x1="384.2" y1="5" x2="384.2" y2="190"/><line x1="420" y1="5" x2="420" y2="190"/>
      </g>
      <g font-size="6.4" fill="#333" text-anchor="end">
        <text x="17" y="7">150</text><text x="17" y="38">125</text><text x="17" y="69">100</text><text x="17" y="100">75</text><text x="17" y="131">50</text><text x="17" y="161">25</text><text x="17" y="192">0</text>
      </g>
      <g font-size="6.4" fill="#333" text-anchor="middle">
        <text x="26" y="204">1995</text><text x="61.8" y="204">2000</text><text x="97.6" y="204">2005</text><text x="133.5" y="204">2010</text><text x="169.3" y="204">2020</text><text x="205.1" y="204">2025</text><text x="240.9" y="204">2030</text><text x="276.7" y="204">2035</text><text x="312.6" y="204">2040</text><text x="348.4" y="204">2045</text><text x="384.2" y="204">2050</text>
      </g>
      <polyline fill="none" stroke="#bbb" stroke-width=".6" points="226.6,116 230,124 234,112 238,126 242,114 246,125 250,117 254,124 258,119 262,123 266,120 272,121"/>
      <polyline fill="none" stroke="#333" stroke-width=".6" points="26,122 29,125 31,110 33,128 35,118 37,126 39,113 41,120 43,124 45,116 47,127 49,119 51,122 53,115 55,125 57,118 59,121 61,114 63,126 65,117 67,122 69,119 71,124 73,112 75,127 77,118 79,121 81,116 83,123 85,120 87,125 89,117 91,121 93,114 95,125 97,104 99,120 101,119 103,113 105,125 107,118 109,122 111,103 113,140 115,90 117,150 119,80 121,145 123,95 125,128 127,115 129,120 131,95 133,150 135,60 137,160 139,85 141,140 143,110 145,120 147,108 149,125 151,90 153,130 155,108 157,125 160,113 163,128 166,110 169,126 172,105 175,130 178,112 181,128 184,100 187,135 190,110 194,126 198,108 202,125 206,112 210,124 214,113 218,122 222,114 226.6,116"/>
      <polyline fill="none" stroke="#e8917f" stroke-width="1" points="226.6,116 240,113 250,112 260,110 270,108 280,106 285,104 295,103 300,98 310,97 315,92 325,90 330,85 335,80 340,80 345,72 355,70 360,60 370,55 375,50 385,45 390,38 400,32 405,25 412,20 415,14 420,13"/>
      <polyline fill="none" stroke="#1d5a97" stroke-width="1.2" points="226.6,116 312.6,146.8 420,190"/>
      <g fill="#1d5a97"><circle cx="226.6" cy="116" r="2.6"/><circle cx="312.6" cy="146.8" r="2.6"/><circle cx="420" cy="190" r="2.6"/></g>
    </symbol>

    <symbol id="timeline" viewBox="0 0 450 26">
      <g fill="#222">
        <path d="M27 5 L31 8 L27 11Z M31 5 L35 8 L31 11Z M26 5h1v6h-1z"/>
        <path d="M64 5 L68 8 L64 11Z M68 5 L72 8 L68 11Z M72 5h1v6h-1z"/>
      </g>
      <rect x="44" y="2" width="13" height="12" fill="#5b8e8f"/>
      <path d="M48 5 L53 8 L48 11Z" fill="#fff"/>
      <rect x="85" y="1" width="56" height="14" fill="#1d5a97" rx="1"/>
      <text x="113" y="10.5" font-size="5.8" fill="#fff" text-anchor="middle">January 2023</text>
      <line x1="150" y1="8" x2="440" y2="8" stroke="#bbb" stroke-width=".6"/>
      <g stroke="#888" stroke-width=".6"><line x1="163" y1="5" x2="163" y2="10"/><line x1="201" y1="5" x2="201" y2="10"/><line x1="240" y1="5" x2="240" y2="10"/><line x1="279" y1="5" x2="279" y2="10"/><line x1="318" y1="5" x2="318" y2="10"/><line x1="356" y1="5" x2="356" y2="10"/><line x1="395" y1="5" x2="395" y2="10"/><line x1="434" y1="5" x2="434" y2="10"/></g>
      <g font-size="5.2" fill="#444" text-anchor="middle"><text x="163" y="21">Jan 2023</text><text x="201" y="21">July2023</text><text x="240" y="21">Jan 2024</text><text x="279" y="21">July2024</text><text x="318" y="21">Jan 2025</text><text x="356" y="21">July2025</text><text x="395" y="21">Jan 2026</text><text x="434" y="21">July2026</text></g>
    </symbol>

    <symbol id="pie-icon" viewBox="0 0 12 12">
      <circle cx="6" cy="6" r="5.5" fill="#2f7fd8"/>
      <path d="M6 6 L6 .5 A5.5 5.5 0 0 1 11.5 6Z" fill="#f2c230"/>
      <path d="M6 6 L11.5 6 A5.5 5.5 0 0 1 8 11.1Z" fill="#3aa85b"/>
    </symbol>

    <symbol id="collapse-icon" viewBox="0 0 10 14">
      <g stroke="#fff" stroke-width="1.3" fill="none"><line x1="1" y1="1" x2="9" y2="1"/><line x1="1" y1="13" x2="9" y2="13"/><polyline points="2,3 5,6 8,3"/><polyline points="2,11 5,8 8,11"/></g>
    </symbol>

    <symbol id="search-icon" viewBox="0 0 10 10">
      <circle cx="4" cy="4" r="3" stroke="#fff" stroke-width="1.2" fill="none"/><line x1="6.3" y1="6.3" x2="9" y2="9" stroke="#fff" stroke-width="1.3"/>
    </symbol>
    <symbol id="gauge-icon" viewBox="0 0 10 10">
      <circle cx="5" cy="5" r="4.5" fill="#fff"/><path d="M5 5 L5 .5 A4.5 4.5 0 0 1 9.5 5Z" fill="#3a3a3a"/>
    </symbol>
  </defs>
</svg>

<main class="board">

  <!-- Screen: mitigation selection -->
  <section class="screen" style="left:97px;top:103px;height:452px">
    <header class="topbar">
      <div class="brand">BRELMONT</div>
      <div class="search">Search<svg width="9" height="9"><use href="#search-icon"/></svg></div>
      <div class="tool-icon chart"><svg width="10" height="10"><use href="#gauge-icon"/></svg></div>
      <div class="tool-icon avatar" role="img" aria-label="User profile photo"></div>
    </header>
    <nav class="sidebar">
      <div class="nav-item">Switch Energy Carrier</div><div class="nav-item active">Energy Efficiency Measures</div><div class="nav-item">Venting To Flare</div><div class="nav-item">Venting To Production</div><div class="nav-item">Fugitive Emissions Measure</div><div class="nav-item">Compressor Replacement</div><div class="nav-item">Reducesd Water Injection</div><div class="nav-item">Drilling Improvements</div><div class="nav-item">Ending Of Pipe Measures</div><div class="nav-item">Company Structure</div><div class="nav-item">Change End Of Life</div><div class="nav-item">New Net Zero Assets</div><div class="nav-item">Update License OwnerShips</div>
    </nav>
    <div class="content">
      <div class="abs h-title" style="left:25px;top:24px">Select A Mitigation Measure</div>
      <div class="abs h-title" style="left:264px;top:96px">Predicted Specific CO2 Emissions</div>
      <svg class="abs" style="left:431px;top:97px" width="12" height="12"><use href="#pie-icon"/></svg>
      <svg class="abs" style="left:20px;top:124px" width="440" height="215"><use href="#emission-chart"/></svg>
      <svg class="abs" style="left:0;top:354px" width="450" height="26"><use href="#timeline"/></svg>
    </div>
  </section>

  <!-- Screen: workbench, base -->
  <section class="screen" style="left:752px;top:103px;height:660px">
    <header class="topbar">
      <div class="brand">BRELMONT</div>
      <div class="search">Search<svg width="9" height="9"><use href="#search-icon"/></svg></div>
      <div class="tool-icon chart"><svg width="10" height="10"><use href="#gauge-icon"/></svg></div>
      <div class="tool-icon avatar" role="img" aria-label="User profile photo"></div>
    </header>
    <nav class="sidebar">
      <div class="nav-item">Switch Energy Carrier</div><div class="nav-item">Energy Efficiency Measures</div><div class="nav-item">Venting To Flare</div><div class="nav-item">Venting To Production</div><div class="nav-item">Fugitive Emissions Measure</div><div class="nav-item active">Compressor Replacement</div><div class="nav-item">Reducesd Water Injection</div><div class="nav-item">Drilling Improvements</div><div class="nav-item">Ending Of Pipe Measures</div><div class="nav-item">Company Structure</div><div class="nav-item">Change End Of Life</div><div class="nav-item">New Net Zero Assets</div><div class="nav-item">Update License OwnerShips</div>
    </nav>
    <div class="content">
      <div class="abs h-title" style="left:22px;top:15px">Compressor rebundling</div>
      <div class="abs assets-title" style="left:22px;top:38px">Assets</div>
      <div class="abs filters" style="left:21px;top:56px"><span class="label">Active Filters</span><span class="chip">Lorem ipsum dolor</span><span class="chip">Lorem ipsum dolor</span><span class="chip">Lorem ipsum dolor</span></div>
      <svg class="abs" style="left:22px;top:78px" width="250" height="170"><use href="#asset-table"/></svg>
      <div class="abs insert" style="left:210px;top:256px">INSERT</div>
      <div class="abs h-title" style="left:300px;top:15px">Parameters</div>
      <div class="abs divider" style="left:361px;top:50px;height:128px"></div>
      <div class="abs param-label" style="left:300px;top:55px">Start</div><div class="abs param-value" style="left:383px;top:52px">January 2023</div>
      <div class="abs param-label" style="left:300px;top:83px">End</div><div class="abs param-value" style="left:383px;top:80px">October 2024</div>
      <div class="abs param-label" style="left:300px;top:111px">Duration</div><div class="abs param-value" style="left:383px;top:108px">21 Month</div>
      <div class="abs param-label" style="left:300px;top:139px">Factor</div><div class="abs param-value" style="left:383px;top:136px">2x</div>
      <div class="abs param-label" style="left:300px;top:166px">Jalla Jalla</div><div class="abs param-check" style="left:407px;top:163px"></div>
      <div class="abs h-title" style="left:22px;top:299px">Predicted Specific CO2 Emissions</div>
      <svg class="abs" style="left:429px;top:299px" width="12" height="12"><use href="#pie-icon"/></svg>
      <svg class="abs" style="left:15px;top:324px" width="440" height="215"><use href="#emission-chart"/></svg>
      <div class="abs legend" style="left:152px;top:548px"><span><i style="background:var(--overage)"></i>Corporate Overage</span><span><i style="background:var(--goals)"></i>Corporate Goals</span></div>
      <svg class="abs" style="left:0;top:569px" width="450" height="26"><use href="#timeline"/></svg>
    </div>
  </section>

  <!-- Screen: workbench, single scenario -->
  <section class="screen" style="left:1407px;top:103px;height:721px">
    <header class="topbar">
      <div class="brand">BRELMONT</div>
      <div class="search">Search<svg width="9" height="9"><use href="#search-icon"/></svg></div>
      <div class="tool-icon chart"><svg width="10" height="10"><use href="#gauge-icon"/></svg></div>
      <div class="tool-icon avatar" role="img" aria-label="User profile photo"></div>
    </header>
    <nav class="sidebar">
      <div class="nav-item">Switch Energy Carrier</div><div class="nav-item">Energy Efficiency Measures</div><div class="nav-item">Venting To Flare</div><div class="nav-item">Venting To Production</div><div class="nav-item">Fugitive Emissions Measure</div><div class="nav-item active">Compressor Replacement</div><div class="nav-item">Reducesd Water Injection</div><div class="nav-item">Drilling Improvements</div><div class="nav-item">Ending Of Pipe Measures</div><div class="nav-item">Company Structure</div><div class="nav-item">Change End Of Life</div><div class="nav-item">New Net Zero Assets</div><div class="nav-item">Update License OwnerShips</div>
    </nav>
    <div class="content">
      <div class="abs h-title" style="left:22px;top:15px">Compressor rebundling</div>
      <div class="abs assets-title" style="left:22px;top:38px">Assets</div>
      <div class="abs filters" style="left:21px;top:56px"><span class="label">Active Filters</span><span class="chip">Lorem ipsum dolor</span><span class="chip">Lorem ipsum dolor</span><span class="chip">Lorem ipsum dolor</span></div>
      <svg class="abs" style="left:22px;top:78px" width="250" height="170"><use href="#asset-table"/></svg>
      <div class="abs insert" style="left:210px;top:256px">INSERT</div>
      <div class="abs h-title" style="left:300px;top:15px">Parameters</div>
      <div class="abs divider" style="left:361px;top:50px;height:128px"></div>
      <div class="abs param-label" style="left:300px;top:55px">Start</div><div class="abs param-value" style="left:383px;top:52px">January 2023</div>
      <div class="abs param-label" style="left:300px;top:83px">End</div><div class="abs param-value" style="left:383px;top:80px">October 2024</div>
      <div class="abs param-label" style="left:300px;top:111px">Duration</div><div class="abs param-value" style="left:383px;top:108px">21 Month</div>
      <div class="abs param-label" style="left:300px;top:139px">Factor</div><div class="abs param-value" style="left:383px;top:136px">2x</div>
      <div class="abs param-label" style="left:300px;top:166px">Jalla Jalla</div><div class="abs param-check" style="left:407px;top:163px"></div>
      <div class="abs h-title" style="left:22px;top:301px">Predicted Specific CO2 Emissions</div>
      <svg class="abs" style="left:429px;top:302px" width="12" height="12"><use href="#pie-icon"/></svg>
      <svg class="abs" style="left:15px;top:324px" width="440" height="215" viewBox="0 0 440 215">
        <use href="#emission-chart" width="440" height="215"/>
        <polyline fill="none" stroke="var(--purple-line)" stroke-width="1" points="226.6,116 240,118 250,121 255,117 262,123 270,119 278,126 285,118 292,124 300,121 308,125 315,120 322,127 330,122 338,128 345,124 352,130 360,127 368,133 378,130 386,135 395,132 402,136 410,134 416,138 420,135"/>
      </svg>
      <div class="abs legend" style="left:152px;top:548px"><span><i style="background:var(--overage)"></i>Corporate Overage</span><span><i style="background:var(--goals)"></i>Corporate Goals</span></div>
      <svg class="abs" style="left:0;top:569px" width="450" height="26"><use href="#timeline"/></svg>
      <div class="scenario-card card-teal" style="left:150px;top:617px;width:174px"><b>Compressor Rebunding</b><small>3/10 Assets included</small><svg width="10" height="14"><use href="#collapse-icon"/></svg></div>
    </div>
  </section>

  <!-- Screen: workbench, stacked scenarios -->
  <section class="screen" style="left:97px;top:620px;height:836px">
    <header class="topbar">
      <div class="brand">BRELMONT</div>
      <div class="search">Search<svg width="9" height="9"><use href="#search-icon"/></svg></div>
      <div class="tool-icon chart"><svg width="10" height="10"><use href="#gauge-icon"/></svg></div>
      <div class="tool-icon avatar" role="img" aria-label="User profile photo"></div>
    </header>
    <nav class="sidebar">
      <div class="nav-item">Switch Energy Carrier</div><div class="nav-item">Energy Efficiency Measures</div><div class="nav-item">Venting To Flare</div><div class="nav-item">Venting To Production</div><div class="nav-item">Fugitive Emissions Measure</div><div class="nav-item active">Compressor Replacement</div><div class="nav-item">Reducesd Water Injection</div><div class="nav-item">Drilling Improvements</div><div class="nav-item">Ending Of Pipe Measures</div><div class="nav-item">Company Structure</div><div class="nav-item">Change End Of Life</div><div class="nav-item">New Net Zero Assets</div><div class="nav-item">Update License OwnerShips</div>
    </nav>
    <div class="content">
      <div class="abs h-title" style="left:22px;top:15px">Compressor rebundling</div>
      <div class="abs assets-title" style="left:22px;top:38px">Assets</div>
      <div class="abs filters" style="left:21px;top:56px"><span class="label">Active Filters</span><span class="chip">Lorem ipsum dolor</span><span class="chip">Lorem ipsum dolor</span><span class="chip">Lorem ipsum dolor</span></div>
      <svg class="abs" style="left:22px;top:78px" width="250" height="170"><use href="#asset-table"/></svg>
      <div class="abs insert" style="left:210px;top:255px">INSERT</div>
      <div class="abs h-title" style="left:299px;top:15px">Parameters</div>
      <div class="abs divider" style="left:361px;top:50px;height:128px"></div>
      <div class="abs param-label" style="left:299px;top:55px">Start</div><div class="abs param-value" style="left:383px;top:52px">January 2023</div>
      <div class="abs param-label" style="left:299px;top:83px">End</div><div class="abs param-value" style="left:383px;top:80px">October 2024</div>
      <div class="abs param-label" style="left:299px;top:111px">Duration</div><div class="abs param-value" style="left:383px;top:108px">21 Month</div>
      <div class="abs param-label" style="left:299px;top:139px">Factor</div><div class="abs param-value" style="left:383px;top:136px">2x</div>
      <div class="abs param-label" style="left:299px;top:166px">Jalla Jalla</div><div class="abs param-check" style="left:407px;top:163px"></div>
      <div class="abs h-title" style="left:22px;top:299px">Predicted Specific CO2 Emissions</div>
      <svg class="abs" style="left:431px;top:300px" width="12" height="12"><use href="#pie-icon"/></svg>
      <svg class="abs" style="left:20px;top:324px" width="440" height="215" viewBox="0 0 440 215">
        <use href="#emission-chart" width="440" height="215"/>
        <polyline fill="none" stroke="var(--purple-line)" stroke-width="1" points="226.6,116 240,120 250,124 260,128 268,126 275,135 282,137 290,131 296,140 305,143 312,145 320,150 327,152 334,155 340,160 347,163 353,160 360,165 366,170 372,168 378,172 385,170 392,174 400,177 406,175 412,180 416,179 420,176"/>
      </svg>
      <div class="abs legend" style="left:152px;top:548px"><span><i style="background:var(--overage)"></i>Corporate Overage</span><span><i style="background:var(--goals)"></i>Corporate Goals</span></div>
      <svg class="abs" style="left:0;top:569px" width="450" height="26"><use href="#timeline"/></svg>
      <div class="scenario-card card-teal" style="left:99px;top:614px;width:174px"><b>Compressor Rebunding</b><small>3/10 Assets included</small><svg width="10" height="14"><use href="#collapse-icon"/></svg></div>
      <div class="scenario-card card-orange" style="left:263px;top:660px;width:183px"><b>Compressor Rebunding</b><small>3/10 Assets included</small><svg width="10" height="14"><use href="#collapse-icon"/></svg></div>
      <div class="scenario-card card-yellow" style="left:24px;top:678px;width:235px"><b>Compressor Rebunding</b><small>3/10 Assets included</small><svg width="10" height="14"><use href="#collapse-icon"/></svg></div>
      <div class="scenario-card card-navy" style="left:24px;top:724px;width:235px"><b>Compressor Rebunding</b><small>3/10 Assets included</small><svg width="10" height="14"><use href="#collapse-icon"/></svg></div>
    </div>
  </section>

  <!-- Screen: workbench, measure timeline -->
  <section class="screen" style="left:752px;top:824px;height:836px">
    <header class="topbar">
      <div class="brand">BRELMONT</div>
      <div class="search">Search<svg width="9" height="9"><use href="#search-icon"/></svg></div>
      <div class="tool-icon chart"><svg width="10" height="10"><use href="#gauge-icon"/></svg></div>
      <div class="tool-icon avatar" role="img" aria-label="User profile photo"></div>
    </header>
    <nav class="sidebar">
      <div class="nav-item">Switch Energy Carrier</div><div class="nav-item">Energy Efficiency Measures</div><div class="nav-item">Venting To Flare</div><div class="nav-item">Venting To Production</div><div class="nav-item">Fugitive Emissions Measure</div><div class="nav-item active">Compressor Replacement</div><div class="nav-item">Reducesd Water Injection</div><div class="nav-item">Drilling Improvements</div><div class="nav-item">Ending Of Pipe Measures</div><div class="nav-item">Company Structure</div><div class="nav-item">Change End Of Life</div><div class="nav-item">New Net Zero Assets</div><div class="nav-item">Update License OwnerShips</div>
    </nav>
    <div class="content">
      <div class="abs h-title" style="left:22px;top:15px">Compressor rebundling</div>
      <div class="abs assets-title" style="left:22px;top:38px">Assets</div>
      <div class="abs filters" style="left:21px;top:56px"><span class="label">Active Filters</span><span class="chip">Lorem ipsum dolor</span><span class="chip">Lorem ipsum dolor</span><span class="chip">Lorem ipsum dolor</span></div>
      <svg class="abs" style="left:22px;top:78px" width="250" height="170"><use href="#asset-table"/></svg>
      <div class="abs insert" style="left:210px;top:256px">INSERT</div>
      <div class="abs h-title" style="left:300px;top:15px">Parameters</div>
      <div class="abs divider" style="left:361px;top:50px;height:128px"></div>
      <div class="abs param-label" style="left:300px;top:55px">Start</div><div class="abs param-value" style="left:383px;top:52px">January 2023</div>
      <div class="abs param-label" style="left:300px;top:83px">End</div><div class="abs param-value" style="left:383px;top:80px">October 2024</div>
      <div class="abs param-label" style="left:300px;top:111px">Duration</div><div class="abs param-value" style="left:383px;top:108px">21 Month</div>
      <div class="abs param-label" style="left:300px;top:139px">Factor</div><div class="abs param-value" style="left:383px;top:136px">2x</div>
      <div class="abs param-label" style="left:300px;top:166px">Jalla Jalla</div><div class="abs param-check" style="left:407px;top:163px"></div>
      <div class="abs h-title" style="left:22px;top:299px">Predicted Specific CO2 Emissions</div>
      <svg class="abs" style="left:429px;top:300px" width="12" height="12"><use href="#pie-icon"/></svg>
      <svg class="abs" style="left:15px;top:324px" width="440" height="215" viewBox="0 0 440 215">
        <use href="#emission-chart" width="440" height="215"/>
        <polyline fill="none" stroke="var(--sky-line)" stroke-width="1" points="226.6,116 236,122 242,130 248,127 252,137 258,130 262,140 268,134 274,141 280,137 286,141 290,145 296,138 302,150 308,143 314,153 320,150 326,158 332,155 338,162 344,158 350,165 356,170 362,166 368,175 372,172 378,177 386,174 392,179 400,183 406,180 414,181 420,182"/>
      </svg>
      <div class="abs legend" style="left:152px;top:548px"><span><i style="background:var(--overage)"></i>Corporate Overage</span><span><i style="background:var(--goals)"></i>Corporate Goals</span></div>
      <svg class="abs" style="left:0;top:569px" width="450" height="26"><use href="#timeline"/></svg>
      <div class="gantt-bar" style="left:149px;top:606px;width:269px;background:var(--bar-red)">Demo Fifld 1</div>
      <div class="gantt-bar" style="left:102px;top:631px;width:276px;background:var(--bar-orange)">Demo Fifld 2</div>
      <div class="gantt-bar" style="left:102px;top:656px;width:276px;background:var(--bar-green)">Demo Fifld 3</div>
      <div class="gantt-bar" style="left:140px;top:681px;width:302px;background:var(--bar-yellow);color:#333">Demo Fifld 4</div>
      <div class="gantt-bar" style="left:102px;top:706px;width:276px;background:var(--bar-blue)">Demo Fifld 5</div>
      <div class="gantt-bar" style="left:169px;top:731px;width:176px;background:var(--bar-slate)">Demo Fifld 2</div>
      <div class="gantt-bar" style="left:169px;top:756px;width:176px;background:var(--bar-violet)">Demo Fifld 3</div>
    </div>
  </section>

</main>
</body>
</html>
```